Wordpress Business Travel Blog and Discussion Board

Oh, Hello!

We are looking for a motivated designer to create a full, turnkey interactive WordPress website geared toward business travel that includes a news style blog (look at ByteHarbor.com and Wirevane.com for the style we like) that is seamlessly integrated with a robust message board (look at JetGabble.com and LoftCabin.com). Ok, so stick with us here because this is actually a pretty cool project that shouldn't be too hard, but yes, of course we have some curve balls that we are throwing your way. Sorry! :)

*On the front page*

- We would like to have a typical news style blog layout that is fun, somewhat professional, and easy to read. That's easy!

- Somewhere within first glance, we would like to have a short list of the most active discussions on our discussion board. (What's trending, or something like that). Not too bad, right?

- Overall, want to have a good amount of content, but we also do not want the visitor to feel as if he or she is having to sift through a lot of content to see what he or she wants to see. Great! We're past the beginning!

We will have traditional visual advertising on all of our pages. Please leave space as necessary :)

*On the Blog/News story pages*

Let's keep these simple - but there is a twist!

Let's say I create a blog/news post. I would like that blog/news post to also be opened as a discussion on the discussion board. For example, I write an article about Corvane Airways and their service on a particular international flight. This will be opened as a discussion under the Corvane Airways topic in the discussion board. Other users can also open new discussions under any topic on the discussion board, but they cannot post stories (unless permission is given) to the blog wall. We would like their posts to show up as regular discussion board posts while the news/blog posts by us show up as news/blog posts on the front page, *and* (oh yes we did!) as discussions in the discussion board. Of course, users will still be able to post comments to the news/blog post, which will also be posted in the discussion.

OK, does that make sense? Let me know if I can help make this more clear! :) Sorry!

*Wiki Pages*

Take a look at the Corvane Airways example above. In that example, my news/blog entry automatically opens a new discussion post. Although we won't necessarily need to create a new wiki page, we would like to tag the post and the discussion to a wiki page about the topic. The wiki page can be created and edited by all users (and locked by us if necessary). BONUS! Can we tag more than one wiki page?

*Websites that inspire us*

ByteHarbor.com - concept and design
Wirevane.com - concept and design
JetGabble.com - concept
LoftCabin.com - concept
pomwhisper.com - concept

All of the sites above are great and we can only thrive with their great success. We are not aiming to be a competitor to the travel sites, but just another great option for interested visitors. Please do not simply copy what they have. What is posted above is a list of our favorite sites that we visit every day.

Our favorite font is Segoe UI, but please don't use this (or a similar font) too much! Maybe just titles would be great. You're the designer so you can make the call here.

Also, our favorite color is blue, but if you have another favorite color, go ahead and show us what you can do! (Don't use too much blue!)

*Oh, and One More Thing*

(I know, you thought we were done. We're not!)

Here's the killer - We would like to create a way for people to, say, enter the details of their next trip and be matched with someone who will also be on a portion of their trip.

For example, let's say I am flying Brisola Airways flight 109 from Los Angeles to New York JFK Airport this Friday. I am staying at the Marrow Lodge Manhattan Central on Friday night, and I am flying back on Saturday night on Quessa flight 290 from New York JFK airport back to Los Angeles. Another user will also be on the Quessa flight back to Los Angeles with me and he entered that information in the website. (Note, the user has to manually enter this information). The other user and I will both be notified that there is at least one other user who will be on the same Quessa flight as me. We will both have the option to reveal our online identity - which will in fact be released to each person as long as each person *mutually* agrees.

This can be very simple - almost like a dating site type of match but it is based on two people being in the same place at the same time (based on what they report). Also, we would like to be able to collect this information - not necessarily tied to the user's true identity. The information we would like to have is - what the user is claiming he or she is doing on the trip (i.e. staying at the Marrow Lodge Central, flying Brisola Airways), and whether or not the user agreed to reveal his or her identity - AND! whether or not the users both revealed their identity.

*Most Important*

HAVE FUN and THANK YOU!! :)

A couple of quick notes - this is a design and code project. We are most likely offering a more $(!) design and code project for the version 2.0 of this website once we get user feedback from this first round.

Also, the name of the website is Veyrola. (www.veyrola.com)

Good luck!

• We need to have a high end, professional, modern, and clean design on the front page to entice readers to constantly visit and stay on our site.
• It would be great to give us the ability to automatically recognize users for visiting the website and/or participating and commenting. Social badges, recognition, etc. would be very cool.
• Although this is a website around business travel, we do not necessarily want it to be business travel themed. There can be hints of the theme, but otherwise the visual look should be somewhat generic.

```html
<!DOCTYPE html>
<html lang="en">
<head>
<meta charset="utf-8">
<title>Veyrola – Travel Blog</title>
<link href="https://fonts.googleapis.com/css2?family=Jost:wght@300;400&family=Oswald:wght@400;500&family=Arimo:wght@400;700&display=swap" rel="stylesheet">
<style>
:root{
  --sky-1:#8fd0e6;
  --sky-2:#3fa6c9;
  --sky-3:#d6eef5;
  --panel:#ffffff;
  --ink:#222222;
  --muted:#666666;
  --line:#cfcfcf;
  --nav-ink:#555555;
  --orange:#f7a21b;
  --orange-dark:#ee8a0c;
  --green:#7cbd2a;
  --footer:#177f9f;
  --footer-ink:#ffffff;
  --photo-beach:#c9b8a0;
  --photo-sea:#9fc6cf;
  --photo-city:#8aa7b8;
  --photo-pool:#3a6fa8;
}
*{box-sizing:border-box;margin:0;padding:0}
html,body{width:866px;height:1200px;overflow:hidden}
body{position:relative;font-family:"Arimo",Arial,sans-serif;color:var(--ink)}
.sky{position:absolute;inset:0;background:
  radial-gradient(ellipse at 20% 30%,var(--sky-3) 0%,transparent 40%),
  radial-gradient(ellipse at 85% 70%,var(--sky-3) 0%,transparent 35%),
  linear-gradient(160deg,var(--sky-1),var(--sky-2) 55%,var(--sky-1))}
.abs{position:absolute}
/* brand */
.brand{left:88px;top:30px;display:flex;align-items:center;gap:10px}
.brand-mark{width:22px;height:22px;background:var(--orange)}
.brand-name{font-family:"Oswald",sans-serif;font-weight:500;font-size:28px;color:#173a4a}
/* utility bar */
.utility{left:560px;top:0;width:230px;height:21px;background:#f2f2f2;border-radius:0 0 14px 14px;display:flex;justify-content:space-around;align-items:center;font-size:9px;font-weight:700;color:#555}
.search{left:594px;top:27px;width:155px;height:19px;background:#fff;border:2px solid #d8d8d8;border-radius:4px;font-size:9px;font-weight:700;color:#555;padding:2px 4px}
/* main panel */
.panel{left:72px;top:102px;width:722px;height:451px;background:var(--panel)}
.nav{left:72px;top:102px;width:722px;height:36px;display:flex;justify-content:center;align-items:center;background:linear-gradient(#fafafa,#e9e9e9)}
.nav a{font-family:"Jost",sans-serif;font-weight:300;font-size:13px;color:var(--nav-ink);text-decoration:none;padding:0 20px;border-right:1px solid #d6d6d6;line-height:30px}
.nav a:last-child{border-right:none}
.hero{left:76px;top:134px;width:714px;height:314px;background:linear-gradient(180deg,#a9cfd8 0%,var(--photo-sea) 35%,#e7e3dc 60%,var(--photo-beach) 100%)}
.hero-arrow{top:270px;width:26px;height:43px;background:#fff;border-radius:4px;box-shadow:0 0 4px rgba(0,0,0,.2);display:flex;align-items:center;justify-content:center}
.hero-arrow.prev{left:49px;border-radius:4px 0 0 4px}
.hero-arrow.next{left:794px;border-radius:0 4px 4px 0}
.hero-shadow{left:80px;top:450px;width:706px;height:12px;background:radial-gradient(ellipse at center,rgba(0,0,0,.15),transparent 70%)}
.thumbs{left:93px;top:472px;display:flex;gap:7px}
.thumb{width:90px;height:65px}
.thumb.city{background:linear-gradient(#c9d9e4,var(--photo-city) 60%,#5b6c6e)}
.thumb.hall{background:linear-gradient(#7eaecf,#3f6f8f 60%,#2d5c7c)}
.thumb.resort{background:linear-gradient(#9cc8e8,#d7c8b0 50%,#3fc1cf)}
.thumb.arch{background:linear-gradient(#2c58a8,#d2e2f3 60%,#6f94c8)}
.thumb-arrow{top:492px}
/* posts */
.post{left:85px;width:443px;height:131px;background:#fff;border:1px solid #bdbdbd;box-shadow:0 0 0 1px #eee}
.post h2{position:absolute;left:6px;top:7px;font-family:"Oswald",sans-serif;font-weight:400;font-size:14px;color:#111}
.post time{position:absolute;left:6px;top:25px;font-size:9px;color:#777}
.post .pic{position:absolute;left:6px;top:38px;width:122px;height:81px;background:linear-gradient(#2f6fbf,#9fb9d8 35%,#c48a58 48%,var(--photo-pool) 60%,#183e7a)}
.post p{position:absolute;left:139px;top:37px;width:291px;font-size:8.4px;line-height:11.5px;color:#666;text-align:justify}
.post .more{position:absolute;left:139px;top:108px;font-size:9px;color:#111;text-decoration:underline}
/* sidebar */
.tabs{left:546px;top:566px;width:232px;height:24px;background:linear-gradient(var(--orange),var(--orange-dark));border-radius:5px 5px 0 0;display:flex;align-items:center;font-family:"Oswald",sans-serif;font-size:11px;color:#fff}
.tabs span{padding:0 8px 0 16px}
.tabs .on{position:relative}
.tabs .on::after{content:"";position:absolute;left:27px;top:17px;border:5px solid transparent;border-top-color:var(--orange-dark)}
.list{left:546px;top:590px;width:232px;height:257px;background:#fff;border:1px solid #bdbdbd;border-top:none;border-radius:0 0 5px 5px}
.item{position:absolute;left:5px;width:210px;height:56px;border-bottom:1px solid #ddd}
.item .pic{position:absolute;left:0;top:8px;width:65px;height:46px;background:linear-gradient(#c9d9e4,var(--photo-city) 60%,#5b6c6e)}
.item p{position:absolute;left:71px;top:8px;width:149px;font-size:8.6px;line-height:11px;text-align:justify}
.item time{position:absolute;left:71px;top:44px;font-size:8.6px}
.ad{left:546px;top:853px;width:232px;height:131px;background:linear-gradient(#fdfdfd 0%,#e9f3f4 50%,#6fc8d6 68%,#e9e1d2 85%,#d6cab6)}
/* footer */
.footer{left:72px;top:1026px;width:722px;height:155px;background:var(--footer);color:var(--footer-ink)}
.footer h3{position:absolute;left:7px;top:12px;font-size:11px;font-weight:400}
.links{position:absolute;top:40px;list-style:none;font-size:8px;line-height:17.4px}
.links li::before{content:"› ";font-weight:700}
.follow{position:absolute;left:566px;top:65px;display:flex;align-items:center;gap:4px;font-size:8px;color:#bfe0ea}
.follow .dot{width:18px;height:18px;border-radius:50%;background:#fff}
.follow span.label{margin-right:4px}
</style>
</head>
<body>
<div class="sky" role="img" aria-label="Bright blue sky with soft white clouds"></div>

<div class="abs brand"><span class="brand-mark"></span><span class="brand-name">Veyrola</span></div>

<div class="abs utility"><span>SIGNIN</span><span>REGISTER</span><span>HELP</span><span>FAQ</span></div>
<div class="abs search">SEARCH</div>

<div class="abs panel"></div>
<nav class="abs nav">
  <a href="#">HOME</a><a href="#">ABOUT</a><a href="#">BLOG</a><a href="#">FORUMS</a><a href="#">SERVICES</a><a href="#">TESTIMONIALS</a><a href="#">CONTACT</a>
</nav>
<div class="abs hero" role="img" aria-label="Family of three playing in the surf on a sunny beach"></div>
<div class="abs hero-shadow"></div>
<div class="abs hero-arrow prev"><svg width="10" height="12"><path d="M9 0V12L0 6Z" fill="var(--green)"/></svg></div>
<div class="abs hero-arrow next"><svg width="10" height="12"><path d="M1 0V12L10 6Z" fill="var(--green)"/></svg></div>

<svg class="abs thumb-arrow" style="left:74px" width="14" height="16"><path d="M12 1L4 8L12 15" stroke="#000" stroke-width="3.5" fill="none"/></svg>
<div class="abs thumbs">
  <div class="thumb city" role="img" aria-label="City bridge and clock tower"></div>
  <div class="thumb hall" role="img" aria-label="Modern waterfront hall"></div>
  <div class="thumb resort" role="img" aria-label="Beach resort hotel"></div>
  <div class="thumb arch" role="img" aria-label="Futuristic white architecture"></div>
  <div class="thumb city" role="img" aria-label="City bridge and clock tower"></div>
  <div class="thumb hall" role="img" aria-label="Modern waterfront hall"></div>
  <div class="thumb resort" role="img" aria-label="Beach resort hotel"></div>
</div>
<svg class="abs thumb-arrow" style="left:775px" width="14" height="16"><path d="M2 1L10 8L2 15" stroke="#000" stroke-width="3.5" fill="none"/></svg>

<article class="abs post" style="top:569px">
  <h2>SIAM BREEZE PHUKET FLIGHTS BEGIN OCT 1</h2>
  <time>September 2, 2012</time>
  <div class="pic" role="img" aria-label="Hotel beside an infinity pool"></div>
  <p>Siam Breeze, the new "light" airline launched by Lantara Airways International, will begin direct flights from Phuket to Bangkok and Chiang Mai on October 1, it was announced yesterday.Siam Breeze, the new "light" airline launched by Lantara Airways International, will begin direct flights from Phuket to Bangkok and Chiang Mai on October 1, it was announced yesterday.will begin direct flights from Phuket to Bangkok .</p>
  <a class="more" href="#">Read more..</a>
</article>
<article class="abs post" style="top:715px">
  <h2>SIAM BREEZE PHUKET FLIGHTS BEGIN OCT 1</h2>
  <time>September 2, 2012</time>
  <div class="pic" role="img" aria-label="Hotel beside an infinity pool"></div>
  <p>Siam Breeze, the new "light" airline launched by Lantara Airways International, will begin direct flights from Phuket to Bangkok and Chiang Mai on October 1, it was announced yesterday.Siam Breeze, the new "light" airline launched by Lantara Airways International, will begin direct flights from Phuket to Bangkok and Chiang Mai on October 1, it was announced yesterday.will begin direct flights from Phuket to Bangkok .</p>
  <a class="more" href="#">Read more..</a>
</article>
<article class="abs post" style="top:860px">
  <h2>SIAM BREEZE PHUKET FLIGHTS BEGIN OCT 1</h2>
  <time>September 2, 2012</time>
  <div class="pic" role="img" aria-label="Hotel beside an infinity pool"></div>
  <p>Siam Breeze, the new "light" airline launched by Lantara Airways International, will begin direct flights from Phuket to Bangkok and Chiang Mai on October 1, it was announced yesterday.Siam Breeze, the new "light" airline launched by Lantara Airways International, will begin direct flights from Phuket to Bangkok and Chiang Mai on October 1, it was announced yesterday.will begin direct flights from Phuket to Bangkok .</p>
  <a class="more" href="#">Read more..</a>
</article>

<div class="abs tabs"><span class="on">POPULAR</span><span>RECENT</span><span>COMMENTS</span><span>TAGS</span></div>
<div class="abs list">
  <div class="item" style="top:0"><div class="pic" role="img" aria-label="City bridge and clock tower"></div><p>Thailand's best beach destination gears up to celebrate its annual vegetarian festival.</p><time>September 28, 2012</time></div>
  <div class="item" style="top:62px"><div class="pic" role="img" aria-label="City bridge and clock tower"></div><p>Thailand's best beach destination gears up to celebrate its annual vegetarian festival.</p><time>September 28, 2012</time></div>
  <div class="item" style="top:124px"><div class="pic" role="img" aria-label="City bridge and clock tower"></div><p>Thailand's best beach destination gears up to celebrate its annual vegetarian festival.</p><time>September 28, 2012</time></div>
  <div class="item" style="top:186px;border-bottom:none"><div class="pic" role="img" aria-label="City bridge and clock tower"></div><p>Thailand's best beach destination gears up to celebrate its annual vegetarian festival.</p><time>September 28, 2012</time></div>
</div>
<div class="abs ad" role="img" aria-label="Advertisement: hammock under palm trees on a beach with the words Travel &amp; Holidaying"></div>

<footer class="abs footer">
  <h3>Quick Links</h3>
  <ul class="links" style="left:12px"><li>Home</li><li>About Us</li><li>Blog</li><li>Forums</li><li>FAQ</li></ul>
  <ul class="links" style="left:174px"><li>Services</li><li>Cities</li><li>Whats trending</li><li>Testimonials</li><li>Contact Us</li></ul>
  <div class="follow"><span class="label">FOLLOW US ON</span><span class="dot"></span><span class="dot"></span><span class="dot"></span></div>
</footer>
</body>
</html>
```